*YO!!! Designers Needed!!* Front Page Cover Needed for a $$Billion Dollar$$ Company

We are a manufacturer of aluminum electrolytic capacitors. We are looking to create a front page cover that will be used on our annual report. We are a publicly listed company and work with many Pinnacle 300 companies, so your work will be viewed by the BIG GUNS and EXECUTIVES around the WORLD! If selected, you may be selected for additional work.

The front page cover should be unique. If elegance, modern, bling, and creativity somehow got together and had a child, that's what the cover page would look like!

Inspired Examples attached. Check them out!

www.velmoro.com

Font styles to use
Sans Serif

Requirements
Must have
• 1. Must include the attached logo. Logo size, color, and placement are at your discretion.

2. Should include the text, '2020 Annual Report'

3. The design should incorporate the use of foil and/or be embossed. The foil can be part of the design or can be the full page. See various examples attached for reference.

4. Shall be in A4 size and vertical orientation.
Nice to have
• Feel free to add any icons or stock photos (for example capacitors or circuit boards) if needed.

Be creative here and don't be afraid to be bold! The end product will be printed and budget is not a limiting factor, so feel free to make it extravagant if needed.

Our slogan is "Think Ahead". This slogan can or cannot be part of the theme.

```html
<!DOCTYPE html>
<html lang="en">
<head>
<meta charset="utf-8">
<title>Velmoro 2020 Annual Report Cover</title>
<link rel="stylesheet" href="https://fonts.googleapis.com/css2?family=Jost:wght@500;600&display=swap">
<style>
  :root {
    --backdrop: #1c1a18;
    --cover-black: #070707;
    --foil-light: #d9c8a0;
    --foil-mid: #b39d6e;
    --foil-deep: #6f5d3a;
    --frame-line: #cfcfcf;
    --ink: #0d0d0d;
  }
  * { box-sizing: border-box; margin: 0; padding: 0; }
  html, body {
    width: 1200px;
    height: 789px;
    overflow: hidden;
    background: var(--backdrop);
  }
  .canvas {
    position: relative;
    width: 1200px;
    height: 789px;
  }
  .cover {
    position: absolute;
    left: 345px;
    top: 34px;
    width: 510px;
    height: 721px;
    background: var(--cover-black);
    font-family: "Jost", "Helvetica Neue", Arial, sans-serif;
    color: var(--ink);
  }
  .foil-splash {
    position: absolute;
    left: 70px;
    top: 190px;
    width: 370px;
    height: 310px;
  }
  .title-frame {
    position: absolute;
    left: 125px;
    top: 218px;
    width: 260px;
    height: 260px;
    border: 1.5px solid var(--frame-line);
  }
  .brand-name {
    position: absolute;
    left: 150px;
    top: 262px;
    width: 210px;
    text-align: right;
    font-size: 48px;
    font-weight: 600;
    line-height: 1;
    letter-spacing: 0.01em;
  }
  .report-title {
    position: absolute;
    left: 170px;
    top: 378px;
  }
  .report-year {
    font-size: 44px;
    font-weight: 500;
    letter-spacing: 0.28em;
    line-height: 1;
  }
  .report-label {
    font-size: 10px;
    font-weight: 500;
    letter-spacing: 0.32em;
    margin-top: 4px;
  }
</style>
</head>
<body>
<main class="canvas">
  <section class="cover">
    <svg class="foil-splash" viewBox="0 0 370 310" role="img" aria-label="Gold foil brush-stroke texture">
      <defs>
        <linearGradient id="foil" x1="0" y1="0" x2="1" y2="1">
          <stop offset="0" stop-color="#b39d6e"/>
          <stop offset="0.35" stop-color="#d9c8a0"/>
          <stop offset="0.6" stop-color="#b39d6e"/>
          <stop offset="0.85" stop-color="#d9c8a0"/>
          <stop offset="1" stop-color="#6f5d3a"/>
        </linearGradient>
      </defs>
      <polygon fill="url(#foil)" points="
        60,20 90,8 110,22 140,4 170,18 200,6 230,20 262,10 290,26 320,18 340,40
        330,62 356,80 338,104 362,126 344,148 366,172 340,196 358,220 332,240
        346,264 312,276 290,300 262,286 232,304 204,288 172,306 140,290 110,302
        86,282 52,292 40,266 12,252 30,226 6,204 28,182 4,160 26,138 8,114 34,96
        14,72 42,56 30,34" />
    </svg>
    <div class="title-frame"></div>
    <div class="brand-name">Velmoro</div>
    <div class="report-title">
      <div class="report-year">2020</div>
      <div class="report-label">ANNUAL REPORT</div>
    </div>
  </section>
</main>
</body>
</html>
```